OK!REELS WEBSITE

I need to get the design for the website of my company, which is a production company based in Los Angeles called OK! REELS. The company works as a liason between Russian speaking and English speaking film communities, providing the spectrum of production services in Eastern Europe and United States of America.
Has to have the following links:
About
Locations
Works
I'd like to see the designs on the white background using the blue and red colors.
Please try to use the font of an old typewriter if you can. You can also get some ideas after looking at the logo, which you need to intergrate into the webdesign anyway.
Thank you very much and I wish you some inspiration!
Updates

I'd like to extend the project till July the 10th, please send more submissions

Reason: I want to give more time to make changes to my comments

Target Market(s)

Production studios from different countries, Directors, Producers, Clients

Industry/Entity Type

It Company

Font styles to use
Sans Serif
Other font styles liked:
• typewriter

Requirements
Must have
• Visible logo design intergrated into graphics

```html
<!DOCTYPE html>
<html lang="en">
<head>
<meta charset="utf-8">
<title>OK! REELS</title>
<link rel="stylesheet" href="https://fonts.googleapis.com/css2?family=Pathway+Gothic+One&display=swap">
<style>
  :root {
    --white: #ffffff;
    --brand-red: #c0202f;
    --brand-blue: #1f6ca3;
    --ink-light: #f4f4f4;
    --hero-dark: #1c1a1b;
    --hero-mid: #4a3a33;
    --hero-skin: #9c7b6a;
    --icon-blue: #2a6fa8;
  }
  * { margin: 0; padding: 0; box-sizing: border-box; }
  html, body { width: 1200px; height: 1125px; overflow: hidden; background: var(--white); }
  body { position: relative; font-family: "Pathway Gothic One", "Arial Narrow", sans-serif; color: var(--white); }

  .hero {
    position: absolute; left: 0; top: 88px; width: 1200px; height: 663px;
    background:
      radial-gradient(ellipse 260px 330px at 610px 260px, var(--hero-skin) 0%, var(--hero-mid) 55%, transparent 100%),
      radial-gradient(ellipse 200px 180px at 200px 570px, #6b4d42 0%, transparent 100%),
      radial-gradient(ellipse 200px 180px at 1050px 570px, #6b4d42 0%, transparent 100%),
      linear-gradient(180deg, #262427 0%, var(--hero-dark) 60%, #2e2523 100%);
  }

  .brand-plate {
    position: absolute; left: 545px; top: 12px; width: 198px; height: 130px;
    background: var(--white);
    display: flex; flex-direction: column; align-items: center; justify-content: center;
    border-bottom: 5px solid var(--brand-blue);
  }
  .brand-name { font-size: 58px; line-height: 1; color: var(--brand-red); letter-spacing: 2px; }

  .main-nav { position: absolute; top: 143px; left: 548px; display: flex; gap: 26px; }
  .main-nav a { font-size: 20px; color: var(--ink-light); text-decoration: none; text-transform: uppercase; }
  .main-nav a.is-active { color: var(--brand-red); }

  .player { position: absolute; top: 528px; left: 0; width: 1200px; }
  .player-control { position: absolute; text-align: center; font-size: 21px; text-transform: uppercase; color: var(--ink-light); width: 140px; }
  .player-control svg { display: block; margin: 0 auto 8px; }
  .control-prev { left: 431px; }
  .control-play { left: 580px; }
  .control-next { left: 694px; }
  .sound-toggle { position: absolute; left: 976px; top: 38px; }

  .social-links { position: absolute; top: 690px; left: 570px; display: flex; gap: 2px; }
  .social-links span { width: 25px; height: 25px; background: var(--icon-blue); display: block; }
  .social-links span.is-hover { background: var(--brand-red); }

  .intro {
    position: absolute; left: 0; top: 751px; width: 1200px; height: 234px;
    background: var(--brand-blue);
  }
  .intro-column { position: absolute; top: 16px; width: 342px; }
  .intro-column.who { left: 202px; }
  .intro-column.what { left: 652px; }
  .intro-column h2 { font-weight: 400; font-size: 19px; text-align: center; text-transform: uppercase; margin-bottom: 10px; }
  .intro-column p { font-size: 12.4px; line-height: 15.7px; color: var(--ink-light); }

  .site-footer { position: absolute; top: 988px; left: 0; width: 1200px; text-align: center; }
  .footer-brand { font-size: 30px; line-height: 1; color: var(--brand-red); display: block; }
  .copyright { font-size: 10px; color: var(--brand-blue); margin-top: 14px; letter-spacing: .2px; }
</style>
</head>
<body>
  <section class="hero" role="img" aria-label="Dark film still: close portrait of a girl with long dark hair, a man's hands resting on her shoulders"></section>

  <header>
    <div class="brand-plate"><span class="brand-name">OK! REELS</span></div>
    <nav class="main-nav">
      <a href="#" class="is-active">About</a>
      <a href="#">Locations</a>
      <a href="#">Works</a>
    </nav>
  </header>

  <div class="player">
    <div class="player-control control-prev">
      <svg width="36" height="22" viewBox="0 0 36 22"><path d="M18 0v22L0 11zM36 0v22L18 11z" fill="#fff"/></svg>
      Previous movie
    </div>
    <div class="player-control control-play">
      <svg width="22" height="24" viewBox="0 0 22 24"><path d="M0 0l22 12L0 24z" fill="#fff"/></svg>
      See&nbsp; extract
    </div>
    <div class="player-control control-next">
      <svg width="36" height="22" viewBox="0 0 36 22"><path d="M0 0v22l18-11zM18 0v22l18-11z" fill="#fff"/></svg>
      Next movie
    </div>
    <svg class="sound-toggle" width="36" height="26" viewBox="0 0 36 26" aria-label="Sound">
      <path d="M0 8h6l8-7v24l-8-7H0z" fill="#fff"/>
      <path d="M20 8q3 5 0 10M25 5q5 8 0 16M30 2q7 11 0 22" stroke="#fff" stroke-width="2" fill="none"/>
    </svg>
  </div>

  <div class="social-links" aria-label="Social links">
    <span></span><span></span><span></span><span></span><span class="is-hover"></span><span></span>
  </div>

  <section class="intro">
    <div class="intro-column who">
      <h2>Who we are ?</h2>
      <p>Lorem ipsum dolor sitamet, consecteturadipiscingelit. Aenean turpis nibh, lacinia vel massa in, pharetra tincidunt libero. Nullameu urna varius nulla viverraornare. Pellentesque quis pharetra dui, aconsequat risus. Donec ligula mi, bibendum in malesuada nec, adipiscingeget purus. Lorem ipsum dolor sitamet, consecteturadipiscingelit. Duis vel molestie mi, sitametconvallis turpis. Quisqueegestas volutpat ligula, etcursus erat imperdiet non. Vivamus mollis enim non tincidunt malesuada. Sed nisieros, mattis vestibulum sem quis, ullamcorpercondimentum justo. Pellentesque dictum vulputate sem quis feugiat. In tristique tellus id mauris lacinia, veleleifend lorem sollicitudin.</p>
    </div>
    <div class="intro-column what">
      <h2>What we do ?</h2>
      <p>Maecenas volutpat mauris vel metus gravidaaliquet. Cum sociis natoque penatibus et magnis dis parturient montes, nascetur ridiculus mus. Interdumet malesuada fames acante ipsum primis in faucibus. Mauris vitae loremeget nulla pretium luctus quis nec urna. Fusce pharetra iaculis mauris, sedconsecteturarcuconsectetur quis. Aeneancursus consequat vulputate. Maecenas turpis mi, mattis vitaeaugue ut, fringilla tempor risus.<br>Nulla sitamet magna sitamet nisl interdumadipiscing veleu risus. Nullameget metus est. Phasellus ac velit feugiat, consequat nulla vitae, sagittis felis. Proin porttitor, doloret</p>
    </div>
  </section>

  <footer class="site-footer">
    <span class="footer-brand">OK! REELS</span>
    <p class="copyright">Copyrights (c) 2014 All Rights Reserved OK! Reels !</p>
  </footer>
</body>
</html>
```